I am a company selling interior designing materials

HI, I am selling interior design materials and require a namecard which is more outstanding while following a certain details placement as attached.

My clients are mainly interior designers so it has to attract their attention rather than feeling that its "just another namecard". I am selling wallcoverings, fabrics, acoustics and carpets.

Target Market(s)

interior designers designing hotels, commerical offices.

Contact Information for Business Card

As per attached.
Please change address to 47 Jalan 16 Tampines #05-02 Velmora Building Singapore 527314

Font styles to use
Other font styles liked:
• calibri

Requirements
Must have
• (1) company logo on top in the middle. Placement of contac details to be the same
• (2) company color is blue/green cymk 75/8/42/0
• (3) "KTV" logo to be prominent
• (4) You may change the logo but there should be a "swirl" surrounding the word KTV like current logo. The swirl pattern does not need to follow current logo and you may propose.
Should not have
• (1) there should not be any designs above "KTV" logo
• (2) no sharp triangles or angles

```html
<!DOCTYPE html>
<html lang="en">
<head>
<meta charset="utf-8">
<title>KTV Business Card</title>
<link rel="stylesheet" href="https://fonts.googleapis.com/css2?family=Carlito:wght@400;700&family=Open+Sans:wght@400;600&family=Roboto:wght@400&display=swap">
<style>
  :root {
    --backdrop: #d4d4d4;
    --card: #ffffff;
    --teal: #26aca2;
    --ink: #5e5e5e;
    --ink-soft: #555555;
    --rule: #6b6b6b;
  }
  * { margin: 0; padding: 0; box-sizing: border-box; }
  html, body { width: 1200px; height: 1200px; overflow: hidden; }
  body { background: var(--backdrop); position: relative; }

  .card {
    position: absolute;
    background: var(--card);
    box-shadow: 0 2px 8px rgba(0,0,0,0.22);
    overflow: hidden;
  }
  .card--front { left: 170px; top: 78px; width: 877px; height: 500px; }
  .card--back  { left: 167px; top: 620px; width: 883px; height: 503px; }

  .brand-name {
    position: absolute; left: 0; right: 0; text-align: center;
    font-family: "Carlito", "Calibri", sans-serif; font-weight: 700;
    color: var(--ink); letter-spacing: 1px;
  }
  .card--front .brand-name { top: 60px; font-size: 62px; line-height: 1; }
  .company {
    position: absolute; left: 0; right: 0; top: 144px; text-align: center;
    font-family: "Carlito", "Calibri", sans-serif; font-weight: 700;
    font-size: 18px; color: var(--ink-soft);
  }
  .person {
    position: absolute; left: 0; right: 0; top: 200px; text-align: center;
    font-family: "Open Sans", sans-serif; font-size: 50px; line-height: 1.1;
    color: var(--teal);
  }
  .person strong { font-weight: 600; }
  .person span { font-weight: 400; }
  .mobile {
    position: absolute; left: 0; right: 0; top: 258px; text-align: center;
    font-family: "Roboto", sans-serif; font-size: 29px; color: var(--ink-soft);
  }
  .divider {
    position: absolute; left: 288px; top: 317px; width: 300px; height: 3px;
    background: radial-gradient(ellipse at center, rgba(0,0,0,0.16) 0%, rgba(0,0,0,0) 70%);
  }
  .contact {
    position: absolute; display: flex; align-items: flex-start; gap: 8px;
    font-family: "Roboto", sans-serif; font-size: 21px; line-height: 30px;
    color: var(--ink-soft);
  }
  .contact svg { flex: none; width: 27px; height: 27px; margin-top: 1px; }
  .contact--address { left: 88px; top: 394px; }
  .contact--phone { left: 486px; top: 386px; }
  .contact--email { left: 486px; top: 422px; }

  .card--back .brand-name { top: 196px; font-size: 128px; line-height: 1; letter-spacing: 2px; }
  .back-rule { position: absolute; left: 0; right: 0; top: 436px; height: 3px; background: var(--rule); }
  .product-band {
    position: absolute; left: 0; right: 0; top: 442px; height: 61px;
    background: var(--teal);
    display: flex; justify-content: center; align-items: center; gap: 24px;
    font-family: "Carlito", "Calibri", sans-serif; font-weight: 700;
    font-size: 21px; color: #ffffff; list-style: none;
  }
  .product-band li::before { content: "\2022"; margin-right: 6px; }
</style>
</head>
<body>

<section class="card card--front">
  <div class="brand-name">KTV</div>
  <div class="company">KelTavo Interior Furnishings Pte Ltd</div>
  <h1 class="person"><strong>Marissa</strong> <span>Teo</span></h1>
  <div class="mobile">(65) 9172 4460</div>
  <div class="divider"></div>

  <div class="contact contact--address">
    <svg viewBox="0 0 28 28" aria-hidden="true">
      <circle cx="14" cy="14" r="12.5" fill="none" stroke="var(--teal)" stroke-width="2"/>
      <path d="M7 14.5 L14 8.5 L21 14.5 H19 V20 H15.5 V16.5 H12.5 V20 H9 V14.5 Z" fill="var(--teal)"/>
    </svg>
    <div>47 Jalan 16 Tampines #05-02<br>Velmora Building Singapore 527314</div>
  </div>

  <div class="contact contact--phone">
    <svg viewBox="0 0 28 28" aria-hidden="true">
      <circle cx="14" cy="14" r="12.5" fill="none" stroke="var(--teal)" stroke-width="2"/>
      <path d="M9.5 7.5 C8 8.5 7.6 10.5 8.8 13 C10.3 16.2 12.8 18.8 15.6 20 C17.8 21 19.6 20.2 20.4 18.8 L18 16.6 C17.5 16.3 17 16.4 16.6 16.9 L15.9 17.6 C14.2 16.8 12.4 15 11.4 13.1 L12.1 12.4 C12.6 11.9 12.7 11.4 12.4 10.9 Z" fill="var(--teal)"/>
    </svg>
    <div>(65) 6281 5074</div>
  </div>

  <div class="contact contact--email">
    <svg viewBox="0 0 28 28" aria-hidden="true">
      <circle cx="14" cy="14" r="12.5" fill="none" stroke="var(--teal)" stroke-width="2"/>
      <rect x="8" y="10" width="12" height="8.5" rx="1" fill="var(--teal)"/>
      <path d="M8.5 10.5 L14 15 L19.5 10.5 M8.5 18 L12.3 13.8 M19.5 18 L15.7 13.8" fill="none" stroke="#fff" stroke-width="1.1"/>
    </svg>
    <div>marissa@ktvfurnishings.com</div>
  </div>
</section>

<section class="card card--back">
  <div class="brand-name">KTV</div>
  <div class="back-rule"></div>
  <ul class="product-band">
    <li>Wallcoverings</li>
    <li>Acoustic</li>
    <li>Fabrics</li>
    <li>Carpet</li>
  </ul>
</section>

</body>
</html>
```